Label for ORGANIC ROSE WATER

Organic Rose Water is a second product from a family of products that we develop. The first product was Organic Argan Oil. The label for this product should be in the same style as the first label that we have. The bottle will be exactly the same. It is good to know that the text should be in GOLD colour (not yellow) it is possible that we continue the same gold or use ROSE (pink) gold. We still have not decided what will suit more.
The fonts that are used in this labels are:
Raleway
and
Butler
both fonts can be found in typemeadow for free
Target Market(s)
Women and girls.
Industry/Entity Type
Cosmetics
Requirements
Must have
- Black label, gold or pink gold colours.
Nice to have
- As this is rose water and the label is minimalistic, the designer should find the best way to input somewhere and somehow rose colour to make the product recognisable.

```html
<!DOCTYPE html>
<html lang="en">
<head>
<meta charset="utf-8">
<title>Organic Rose Water – Label</title>
<link href="https://fonts.googleapis.com/css2?family=Raleway:wght@500&family=Oswald:wght@500&family=Roboto+Condensed:wght@400&family=Kaushan+Script&display=swap" rel="stylesheet">
<style>
  :root {
    --paper: #ffffff;
    --label-black: #0c0a0b;
    --gold: #c9a46a;
    --rose-pink: #ef6fa6;
    --soft-pink: #f3a3c6;
    --ivory: #f4ece4;
    --rose-light: #f7c3d6;
    --rose-deep: #d9497f;
  }
  * { margin: 0; padding: 0; box-sizing: border-box; }
  html, body { width: 1200px; height: 1073px; overflow: hidden; background: var(--paper); }
  .canvas { position: relative; width: 1200px; height: 1073px; }

  .label {
    position: absolute; left: 380px; top: 140px;
    width: 440px; height: 800px;
    background: var(--label-black);
  }

  .brand {
    position: absolute; left: 60px; top: 70px;
    display: flex; align-items: center; gap: 26px;
  }
  .brand-mark { width: 96px; height: 96px; border-radius: 50%; background: var(--rose-pink); }
  .brand-name {
    font-family: "Raleway", sans-serif; font-weight: 500;
    font-size: 50px; color: var(--gold); letter-spacing: 1px;
  }

  .title { position: absolute; left: 0; top: 228px; width: 100%; text-align: center; }
  .title-organic {
    font-family: "Oswald", sans-serif; font-weight: 500;
    font-size: 24px; color: var(--rose-pink); letter-spacing: 0.5px;
    display: block; margin-left: -30px;
  }
  .title-rose {
    font-family: "Kaushan Script", cursive;
    font-size: 116px; line-height: 1; color: var(--rose-pink);
    display: block; margin-top: -6px;
  }
  .title-water {
    font-family: "Oswald", sans-serif; font-weight: 500;
    font-size: 52px; color: var(--gold); letter-spacing: 14px;
    display: block; margin-top: 4px; padding-left: 14px;
  }

  .claim {
    position: absolute; left: 96px; top: 530px;
    font-family: "Roboto Condensed", sans-serif;
    font-size: 21px; line-height: 1.3; color: var(--ivory);
  }
  .claim .latin { padding-left: 38px; }

  .divider { position: absolute; left: 92px; top: 590px; width: 270px; height: 10px; }

  .translations {
    position: absolute; left: 92px; top: 614px;
    font-family: "Roboto Condensed", sans-serif;
    font-size: 21px; line-height: 1.3; color: var(--soft-pink);
  }

  .volume {
    position: absolute; left: 92px; top: 716px;
    font-family: "Roboto Condensed", sans-serif;
    font-size: 21px; line-height: 1.25; color: var(--ivory);
  }

  .rose-visual {
    position: absolute; left: 258px; top: 662px;
    width: 120px; height: 112px; border-radius: 50%;
    background: radial-gradient(circle at 50% 45%, var(--rose-deep) 0%, var(--rose-pink) 40%, var(--rose-light) 85%);
  }
</style>
</head>
<body>
<main class="canvas">
  <section class="label">
    <div class="brand">
      <span class="brand-mark"></span>
      <span class="brand-name">velmora</span>
    </div>

    <h1 class="title">
      <span class="title-organic">ORGANIC</span>
      <span class="title-rose">Rose</span>
      <span class="title-water">WATER</span>
    </h1>

    <p class="claim">100% pure and natural<br><span class="latin">Rosa Damascena</span></p>

    <svg class="divider" viewBox="0 0 270 10" aria-hidden="true">
      <line x1="0" y1="9" x2="270" y2="9" stroke="#ef6fa6" stroke-width="2"/>
      <rect x="6" y="2" width="24" height="7" fill="#ef6fa6"/>
    </svg>

    <p class="translations">BIO Rosenwasser<br>Eau de Rose BIO</p>

    <p class="volume">100ml E<br>3.38 fl.oz</p>

    <div class="rose-visual" role="img" aria-label="Pink Damask rose blossom illustration"></div>
  </section>
</main>
</body>
</html>
```